Postcard for Lawn service business

I am starting a lawn service business and need a professional looking postcard with a logo.

Thank you for any help you can provide.

We are looking for someone to design a long term professional marketable original business logo. One that can be trademarked in the future. Right now we are going with “the silver furrow” lawn service. This is a new start up company that will provide mowing and basic lawn service care as well as full service maintenance on other shrubs/plants on residential property.

We are also looking for a professional looking glossy oversized postcard to direct mail to potential customers through NMDR mail routes. I am open to any professional design ideas, we've provided actual pictures of grass and myself. I would like to keep it personal to the working homeowner, possible small family that doesn’t need to bother with this weekly chore.

Here is an idea for a slogan: "You work hard, let us take care of your yard". Or if you have a better idea.

Suggested verbiage (we like all of them but all may not fit):
Free Estimates- Evening and Weekend Appointments available Call 555-208-4419 or Email TheSilverFurrow@quillpost.com
Services to fit your needs; Basic and Full Service rates available
Fertilization and Maintenance Services for Residential Properties in Corona
Services offered: Mow/Edge/Blow, Fertilization, Weed Control, Yard Cleanups, Hedge Trimming,
Family and Locally owned and operated
Referral savings opportunity! For each friend that receives our monthly lawn service, save $5 off your monthly service for a max savings of $20 a month. Keep this monthly discount for as long as your friends are our customers!

Target Market(s)

We are targeting dual income families that can save time by having someone else provide care for their lawn. We need catchy call to action lines to get them to switch to our service vs their current lawn care providers.

Industry/Entity Type

Residential

Requirements
Must have
• The flyer must be a two sided colorful oversized postcard.
Nice to have
• Would like to see the pantone green used with white throughout the flyer.
PANTONE
16-6138 TCX

Would like similar color feel as flyer2 (file attached)
We like to call-outs feel on flyer3 (file attached)
Img 2150 is a pic of me with our lawn, either keep the whole pic or just me
Dustin1 is a pic of me digging up a tree stump
lawn1, lawn2, lawn3, and lawn4 are shots of grass, can be used as background or something else

```html
<!DOCTYPE html>
<html lang="en">
<head>
<meta charset="utf-8">
<title>The Silver Furrow – Lawn Service Postcard</title>
<link rel="stylesheet" href="https://fonts.googleapis.com/css2?family=Lato:wght@400;700;900&display=swap">
<style>
  :root {
    --stage: #5e5e5e;
    --leaf: #7db23b;
    --leaf-light: #a6cf63;
    --leaf-deep: #4f7d1f;
    --panel: #5b8a25;
    --accent: #e8561b;
    --ink: #222222;
    --paper: #ffffff;
    --stamp: #e6e6e6;
    --rule: #555555;
  }
  * { box-sizing: border-box; margin: 0; padding: 0; }
  html, body {
    width: 1200px; height: 664px; overflow: hidden;
    background: var(--stage);
    font-family: "Lato", Arial, sans-serif;
  }
  .canvas { position: relative; width: 1200px; height: 664px; }

  .card {
    position: absolute; background: var(--paper); overflow: hidden;
    box-shadow: 0 4px 14px rgba(0,0,0,.35);
  }
  .card--front { left: 52px; top: 52px; width: 453px; height: 568px; }
  .card--back  { left: 565px; top: 118px; width: 568px; height: 437px; }

  /* front */
  .front__band {
    position: absolute; left: 0; top: 0; width: 100%; height: 126px;
    background: linear-gradient(180deg, var(--leaf-light), var(--leaf));
  }
  .headline {
    position: absolute; left: 28px; top: 16px;
    font-weight: 900; font-size: 31px; line-height: 35px; color: var(--paper);
  }
  .headline__accent { color: var(--accent); }
  .brand {
    position: absolute; right: 14px; top: 20px; text-align: center;
    font-weight: 700; font-size: 24px; line-height: 30px; color: var(--paper);
  }
  .photo {
    position: absolute; border: 4px solid #eeeeee; border-radius: 6px;
    background: linear-gradient(180deg, #7aa3c8 0%, #5f7f3a 40%, #3f6e1c 100%);
  }
  .front__photo--a { left: 220px; top: 93px; width: 108px; height: 98px; }
  .front__photo--b { left: 336px; top: 93px; width: 108px; height: 98px; }
  .front__worker {
    position: absolute; left: 10px; top: 126px; width: 206px; height: 238px;
    background: linear-gradient(160deg, #3f6f25, #7aa348 60%, #8f9a55);
  }
  .contact {
    position: absolute; right: 12px; top: 192px; text-align: right;
    font-size: 12.5px; line-height: 17px; color: var(--ink);
  }
  .contact__lead { color: var(--accent); font-weight: 700; font-size: 14px; }
  .contact__label { color: var(--accent); }
  .contact__value { color: var(--leaf); font-weight: 700; font-size: 14px; }
  .front__family {
    position: absolute; left: 238px; top: 282px; width: 208px; height: 260px;
    background: radial-gradient(ellipse at 50% 60%, #6b6b6b, #dfe6d6 75%, var(--paper));
  }
  .services {
    position: absolute; left: 10px; top: 368px; width: 206px; height: 156px;
    background: var(--panel); padding: 8px 8px; color: var(--paper);
    font-size: 10.5px; line-height: 12.5px;
  }
  .services__title { color: #f07a2c; font-weight: 700; font-size: 13px; line-height: 15px; }
  .services p + .services__title { margin-top: 8px; }
  .grass {
    position: absolute; left: 0; bottom: 0; width: 100%;
    background: linear-gradient(180deg, rgba(255,255,255,0), #8fcf3e 45%, #3d8a14);
  }
  .card--front .grass { height: 62px; }

  /* back */
  .back__band {
    position: absolute; left: 0; top: 0; width: 315px; height: 148px;
    background: linear-gradient(180deg, var(--leaf-light), var(--leaf));
  }
  .back__photo--a { left: 15px; top: 30px; width: 136px; height: 124px; }
  .back__photo--b { left: 160px; top: 30px; width: 136px; height: 124px; }
  .referral {
    position: absolute; left: 20px; top: 188px; width: 290px; text-align: center;
    font-size: 15px; line-height: 19.5px; color: var(--ink);
  }
  .referral__hot { color: var(--accent); font-weight: 900; font-size: 17px; }
  .stamp {
    position: absolute; left: 478px; top: 12px; width: 75px; height: 83px;
    background: var(--stamp);
  }
  .address-lines { position: absolute; left: 337px; top: 237px; width: 216px; }
  .address-lines span { display: block; height: 37.5px; border-bottom: 1px solid var(--rule); }
  .card--back .grass { height: 100px; }
</style>
</head>
<body>
<main class="canvas">

  <section class="card card--front" aria-label="Postcard front">
    <div class="front__band"></div>
    <h1 class="headline">You work hard,<br>
      <span class="headline__accent">let us take care<br>of your yard</span></h1>
    <div class="brand">Silver<br>Furrow</div>
    <div class="photo front__photo--a" role="img" aria-label="Photo of a mowed lawn with trees"></div>
    <div class="photo front__photo--b" role="img" aria-label="Photo of a shade tree over green lawn"></div>
    <div class="front__worker" role="img" aria-label="Photo of the owner digging up a tree stump with a tiller"></div>
    <div class="contact">
      <div class="contact__lead">Free Estimates-</div>
      <div>Evening and Weekend</div>
      <div>Appointments available</div>
      <div><span class="contact__label">Call</span> <span class="contact__value">555-208-4419</span> or</div>
      <div><span class="contact__label">Email</span> <span class="contact__value">TheSilverFurrow@quillpost.com</span></div>
    </div>
    <div class="front__family" role="img" aria-label="Photo of the owner sitting on a rock with his young daughter"></div>
    <div class="services">
      <h2 class="services__title">Services to fit your needs:</h2>
      <p>Basic and Full Service rates available Fertilization and Maintenance Services for Residential Properties in Corona</p>
      <h2 class="services__title">Services offered:</h2>
      <p>Mow/Edge/Blow, Fertilization, Weed Control, Yard Cleanups, Hedge Trimming,Family and Locally owned and operated</p>
    </div>
    <div class="grass" role="img" aria-label="Band of green grass blades"></div>
  </section>

  <section class="card card--back" aria-label="Postcard back">
    <div class="back__band"></div>
    <div class="photo back__photo--a" role="img" aria-label="Photo of a mowed lawn with trees"></div>
    <div class="photo back__photo--b" role="img" aria-label="Photo of a shade tree over green lawn"></div>
    <p class="referral">Referral savings opportunity! For each friend that receives our monthly lawn service, <span class="referral__hot">save $5</span> off your monthly service for a <span class="referral__hot">max savings of $20</span> a month. Keep this monthly discount for as long as your friends are our customers!</p>
    <div class="stamp"></div>
    <div class="address-lines"><span></span><span></span><span></span><span></span></div>
    <div class="grass" role="img" aria-label="Band of green grass blades"></div>
  </section>

</main>
</body>
</html>
```